Professional Report Cover

We need a cover for CFO report (the document is about 20 pages, in case you decide to provide 3D mockup). The design must be professional. The main color has to be #299FC0, which can be incorporated with white, #375172, and #E3E7EE. See attached for content and logo.

```html
<!DOCTYPE html>
<html lang="en">
<head>
<meta charset="UTF-8">
<title>The CFO Insight – Report Cover</title>
<link href="https://fonts.googleapis.com/css2?family=Poppins:wght@500;600;700;800&display=swap" rel="stylesheet">
<style>
  :root {
    --brand-blue: #299FC0;
    --navy: #375172;
    --mist: #E3E7EE;
    --white: #FFFFFF;
    --page-bg: #F4F6F9;
    --ink-soft: #6B7A90;
  }
  * { margin: 0; padding: 0; box-sizing: border-box; }
  html, body {
    width: 887px;
    height: 1200px;
    overflow: hidden;
    background: var(--page-bg);
  }
  .report-cover {
    position: relative;
    width: 887px;
    height: 1200px;
    background: linear-gradient(180deg, var(--white) 0%, #FAFBFD 60%, var(--mist) 100%);
    font-family: "Poppins", Arial, sans-serif;
    overflow: hidden;
  }
  .hero-illustration {
    position: absolute;
    left: 70px;
    top: 300px;
    width: 747px;
    height: 360px;
    border-radius: 180px;
    background: radial-gradient(ellipse at center, rgba(41,159,192,0.22) 0%, rgba(227,231,238,0.85) 55%, rgba(227,231,238,0) 78%);
  }
  .cover-title {
    position: absolute;
    left: 0;
    top: 250px;
    width: 100%;
    text-align: center;
    color: var(--navy);
    line-height: 1;
  }
  .cover-title .title-lead {
    display: block;
    font-size: 92px;
    font-weight: 700;
    letter-spacing: 2px;
  }
  .cover-title .title-main {
    display: block;
    margin-top: 70px;
    font-size: 150px;
    font-weight: 800;
    letter-spacing: 4px;
  }
  .cover-title .title-sub {
    display: block;
    margin-top: 30px;
    font-size: 138px;
    font-weight: 800;
    letter-spacing: 3px;
  }
  .title-rule {
    position: absolute;
    left: 383px;
    top: 770px;
    width: 120px;
    height: 6px;
    border-radius: 3px;
    background: var(--brand-blue);
  }
  .company-mark {
    position: absolute;
    left: 0;
    top: 900px;
    width: 100%;
    display: flex;
    flex-direction: column;
    align-items: center;
  }
  .company-mark .name-row {
    display: flex;
    align-items: center;
    gap: 16px;
  }
  .company-mark .mark-square {
    width: 34px;
    height: 34px;
    background: var(--brand-blue);
  }
  .company-mark .company-name {
    font-size: 34px;
    font-weight: 700;
    color: var(--navy);
    letter-spacing: 1px;
    line-height: 1.1;
    text-align: left;
  }
  .company-mark .group-line {
    margin-top: 18px;
    font-size: 15px;
    font-weight: 500;
    letter-spacing: 4px;
    color: var(--ink-soft);
  }
</style>
</head>
<body>
  <main class="report-cover">
    <div class="hero-illustration" role="img" aria-label="Illustration of business people working around floating finance and technology icons"></div>

    <h1 class="cover-title">
      <span class="title-lead">THE</span>
      <span class="title-main">CFO</span>
      <span class="title-sub">INSIGHT</span>
    </h1>

    <div class="title-rule"></div>

    <div class="company-mark">
      <div class="name-row">
        <span class="mark-square"></span>
        <span class="company-name">NORTHVALE<br>DOCUMENT SERVICES</span>
      </div>
      <p class="group-line">A MERIDIAN GROUP COMPANY</p>
    </div>
  </main>
</body>
</html>
```